Business Card Design

It is an assisted living facility. I wanted the name to reflect that we are a step above other facilities; i.e., professionally decorated rooms, cloth napkins, family dinners, etc. My motto is: COME WHERE YOU ARE CELEBRATED! Also, I have thought about having a house held with the "Hands" and the motto around it but I have seen that logo used other places. In other words, HELP!

I do not have a photo yet, but the photographer is coming next week. I would like the back of the card to have a picture of the facility.

Industry/Entity Type

Business

Contact Information for Business Card

BRIGHT MEADOW ASSISTED LIVING, LLC, 2938 Quillmont Dr., FL 33482-7261
Phone: (555) 214-6037; Fax: (555)
Linda Pruett, Owner/Administrator

```html
<!DOCTYPE html>
<html lang="en">
<head>
<meta charset="utf-8">
<title>Bright Meadow Assisted Living – Business Card</title>
<link rel="stylesheet" href="https://fonts.googleapis.com/css2?family=Open+Sans:wght@400;600;700&display=swap">
<style>
  :root {
    --ink: #2b2b2d;
    --charcoal: #333335;
    --brand-red: #d3203a;
    --paper: #ffffff;
    --backdrop: #e8e8e9;
    --hatch: #d9d9db;
  }
  html, body {
    margin: 0;
    width: 1200px;
    height: 900px;
    overflow: hidden;
    background: var(--backdrop);
    font-family: "Open Sans", Arial, sans-serif;
  }
  .business-card {
    position: absolute;
    left: 100px;
    top: 164px;
    width: 1000px;
    height: 572px;
    background: var(--paper);
    box-shadow: 0 10px 30px rgba(0,0,0,0.12);
    overflow: hidden;
  }
  .card-shapes {
    position: absolute;
    inset: 0;
  }
  .company-name {
    position: absolute;
    left: 58px;
    top: 232px;
    margin: 0;
    font-size: 29px;
    font-weight: 600;
    letter-spacing: 0.2px;
    color: var(--brand-red);
  }
  .address {
    position: absolute;
    left: 58px;
    top: 306px;
    display: flex;
    align-items: center;
    gap: 8px;
    font-size: 16px;
    color: var(--ink);
  }
  .address svg { width: 13px; height: 18px; }
  .name-block {
    position: absolute;
    right: 108px;
    top: 190px;
    text-align: right;
  }
  .person-name {
    margin: 0;
    font-size: 36px;
    line-height: 1.1;
    font-weight: 400;
    color: var(--ink);
  }
  .person-name .first-name { font-weight: 700; }
  .person-role {
    margin: 2px 0 0;
    font-size: 15px;
    letter-spacing: 0.3px;
    color: var(--brand-red);
  }
  .contact-list {
    position: absolute;
    right: 92px;
    top: 376px;
    margin: 0;
    padding: 0;
    list-style: none;
    text-align: right;
  }
  .contact-line {
    display: flex;
    justify-content: flex-end;
    align-items: center;
    gap: 10px;
    font-size: 20px;
    color: var(--ink);
    height: 36px;
  }
  .contact-line svg { width: 20px; height: 18px; }
</style>
</head>
<body>
  <article class="business-card">
    <svg class="card-shapes" viewBox="0 0 1000 572" aria-hidden="true">
      <defs>
        <pattern id="hatch-lines" width="8" height="8" patternUnits="userSpaceOnUse" patternTransform="rotate(45)">
          <rect width="8" height="8" fill="#f3f3f4"/>
          <line x1="0" y1="0" x2="0" y2="8" stroke="var(--hatch)" stroke-width="2"/>
        </pattern>
      </defs>
      <polygon class="name-tab" points="575,172 925,172 925,292 630,292" fill="url(#hatch-lines)"/>
      <rect class="name-tab-accent" x="925" y="172" width="75" height="120" fill="var(--brand-red)"/>
      <rect class="bottom-band" x="330" y="462" width="670" height="80" fill="var(--brand-red)"/>
      <polygon class="corner-band" points="0,352 300,352 395,462 395,572 0,572" fill="var(--charcoal)"/>
    </svg>

    <h1 class="company-name">BRIGHT MEADOW ASSISTED LIVING, LLC</h1>

    <div class="address">
      <svg viewBox="0 0 12 18"><path d="M6 0C2.7 0 0 2.6 0 5.9 0 10.3 6 18 6 18s6-7.7 6-12.1C12 2.6 9.3 0 6 0zm0 8.4A2.5 2.5 0 1 1 6 3.4a2.5 2.5 0 0 1 0 5z" fill="var(--brand-red)"/></svg>
      <span>2938 Quillmont Dr., FL 33482-7261</span>
    </div>

    <div class="name-block">
      <p class="person-name"><span class="first-name">Linda</span> Pruett</p>
      <p class="person-role">OWNER/ADMINISTRATOR</p>
    </div>

    <ul class="contact-list">
      <li class="contact-line">
        <span>(555)</span>
        <svg viewBox="0 0 20 18" aria-label="Fax"><rect x="5" y="0" width="10" height="6" fill="var(--brand-red)"/><rect x="0" y="6" width="20" height="8" rx="2" fill="var(--brand-red)"/><rect x="4" y="11" width="12" height="7" fill="var(--brand-red)" stroke="#fff" stroke-width="1"/></svg>
      </li>
      <li class="contact-line">
        <span>(555) 214-6037</span>
        <svg viewBox="0 0 20 18" aria-label="Phone"><path d="M1 5c0-2 4-4 9-4s9 2 9 4v2h-5V5H6v2H1z" fill="var(--brand-red)"/><path d="M5 8h10l3 9H2z" fill="var(--brand-red)"/><circle cx="10" cy="12.5" r="2.2" fill="#fff"/></svg>
      </li>
    </ul>
  </article>
</body>
</html>
```